BRAND BOOK design

We are a new swimwear brand. We have a vague idea of what we want. We have some colors we would like to use. We would love someone who can provide simple, sophisticated yet an edgy design for our first brand book. The brand book will contain our campaign photos and you will have to come up with layouts and simple designs to insert these photos and short quotes or descriptions. The brand book will contain our brand identity and express the vibes we want our customers to feel get from our brand.

Target Market(s)

US and Australia

Industry/Entity Type

Fashion

Font styles to use
Other font styles liked:
• Futura Medium

Colors
f9d9e8
cfcfcf
ffffff

Requirements
Must have
• simple modern layout with pop elements.
• photos must be placed with enough space.
• also need minimal space for words.
Nice to have
• Simple layouts that aren't common. Designs that can show our identity.
• Please refer to our website (under construction): www.corvanthelabels.com
Should not have
• mere copies of other brand designs

```html
<!DOCTYPE html>
<html lang="en">
<head>
<meta charset="utf-8">
<title>Corvanthe Brand Book Spreads</title>
<link href="https://fonts.googleapis.com/css2?family=Jost:wght@300;400;500&display=swap" rel="stylesheet">
<style>
  :root {
    --blush: #f9d9e8;
    --blush-deep: #e8bfd1;
    --silver: #cfcfcf;
    --paper: #ffffff;
    --mist: #f1f1f1;
    --ink: #4a4a4a;
    --ghost: #e2e2e2;
    --bg: #8a8b9c;
    --teal: #3fa7c2;
    --gold: #d4a640;
  }
  * { margin: 0; padding: 0; box-sizing: border-box; }
  html, body { width: 1200px; height: 1200px; overflow: hidden; }
  body {
    background: var(--bg);
    font-family: "Jost", "Futura", sans-serif;
    color: var(--ink);
    position: relative;
  }
  .spread {
    position: absolute; left: 50px; width: 1100px; height: 420px;
    background: var(--paper);
    box-shadow: 0 10px 30px rgba(0,0,0,.25);
    overflow: hidden;
  }
  .spread--one { top: 150px; }
  .spread--two { top: 650px; }
  .spread::after {
    content: ""; position: absolute; left: 549px; top: 0; width: 2px; height: 100%;
    background: rgba(0,0,0,.08);
  }
  .block { position: absolute; }
  .photo { position: absolute; }
  .band-pink { background: var(--blush-deep); }
  .band-silver { background: var(--silver); }
  .panel-mist { background: var(--mist); }
  .wordmark-vertical {
    position: absolute;
    font-weight: 300; font-size: 60px; letter-spacing: 3px;
    color: transparent; -webkit-text-stroke: 1px #c4c4c4;
    transform: rotate(-90deg); transform-origin: left top;
    white-space: nowrap; line-height: 1;
  }
  .product-tag {
    position: absolute; font-size: 9px; line-height: 1.3; color: var(--ink);
    display: flex; gap: 6px; white-space: nowrap;
  }
  .product-tag--small { font-size: 8px; gap: 5px; }
  .product-tag .dot {
    width: 9px; height: 9px; border-radius: 50%; background: var(--gold); flex: none; margin-top: 1px;
  }
  .product-tag .brand { font-weight: 500; letter-spacing: 1px; }
  .product-tag .price { margin-left: 50px; }
  .product-tag--light { color: #fff; }
  .pink-card { position: absolute; background: var(--blush-deep); }
  .pink-card__shadow { position: absolute; background: var(--silver); }
  .body-copy { position: absolute; font-size: 9.5px; line-height: 1.35; color: var(--ink); }
  .body-copy--center { text-align: center; }
  .star { position: absolute; }
</style>
</head>
<body>

<section class="spread spread--one">
  <div class="product-tag" style="left:22px; top:20px;">
    <span class="dot"></span>
    <div><span class="brand">CORVANTHE</span><br>ART. 45897 BIKINI BOTTOMS<br>92% Polyamid + 8% Elastan<br>new Collection 2018<br>PRICE<span class="price">€ 20.00</span></div>
  </div>
  <div class="photo" role="img" aria-label="Model in pale blue one-piece swimsuit reclining on a white towel beside palm fronds" style="left:14px; top:92px; width:250px; height:316px; background:linear-gradient(160deg,#e9dccd 0%,#d9c5b1 45%,#5f7a3a 80%,#2f4d22 100%);"></div>
  <svg class="block" style="left:214px; top:92px;" width="50" height="50" viewBox="0 0 50 50"><polygon points="0,0 50,0 50,50" fill="var(--teal)"/></svg>

  <div class="photo" role="img" aria-label="Model kneeling in pale blue strappy-back swimsuit among palm plants" style="left:270px; top:14px; width:238px; height:370px; background:linear-gradient(170deg,#3a3f2c 0%,#4f6b35 40%,#c9cfd4 75%,#eef0f1 100%);"></div>
  <div class="product-tag product-tag--light" style="left:280px; top:24px;">
    <span class="dot"></span>
    <div><span class="brand">CORVANTHE</span><br>ART. 45897 BIKINI BOTTOMS<br>92% Polyamid + 8% Elastan<br>new Collection 2018<br>PRICE<span class="price">€ 20.00</span></div>
  </div>

  <div class="block band-pink" style="left:508px; top:0; width:12px; height:420px;"></div>
  <div class="block band-silver" style="left:520px; top:0; width:30px; height:420px;"></div>

  <div class="wordmark-vertical" style="left:612px; top:405px;">CORVANTHE</div>

  <div class="photo" role="img" aria-label="Model in white strappy-back one-piece and sun hat beside a pool" style="left:690px; top:0; width:240px; height:420px; background:linear-gradient(180deg,#6f93c4 0%,#b8c7d6 35%,#2b3c3a 65%,#1d2a2a 100%);"></div>

  <div class="block panel-mist" style="left:930px; top:0; width:170px; height:420px;"></div>
  <div class="pink-card__shadow" style="left:945px; top:140px; width:155px; height:16px;"></div>
  <div class="pink-card" style="left:945px; top:0; width:155px; height:140px;"></div>
  <p class="body-copy body-copy--center" style="left:952px; top:10px; width:141px;">Lorem ipsum dolor sit amet, omnium consulatu repudiandae cu his. Rebum hendrerit ullamcorper usu ad, eruditi imperdiet vis ad, cu fabellas partiendo pro.</p>
  <div class="product-tag product-tag--small" style="left:952px; top:92px;">
    <span class="dot"></span>
    <div>ART. 45897 BIKINI BOTTOMS<br>92% Polyamid + 8% Elastan<br>new Collection 2018<br>PRICE<span class="price" style="margin-left:30px">€ 20.00</span></div>
  </div>
  <svg class="star" style="left:990px; top:260px;" width="100" height="95" viewBox="0 0 100 95"><polygon points="50,0 62,35 100,36 70,58 81,95 50,73 19,95 30,58 0,36 38,35" fill="var(--ghost)"/></svg>
</section>

<section class="spread spread--two">
  <svg class="star" style="left:250px; top:40px;" width="140" height="133" viewBox="0 0 100 95"><polygon points="50,0 62,35 100,36 70,58 81,95 50,73 19,95 30,58 0,36 38,35" fill="var(--ghost)"/></svg>
  <svg class="star" style="left:300px; top:250px;" width="60" height="57" viewBox="0 0 100 95"><polygon points="50,0 62,35 100,36 70,58 81,95 50,73 19,95 30,58 0,36 38,35" fill="var(--ghost)"/></svg>
  <div class="photo" role="img" aria-label="Model in pink bandeau bikini with towel wrapped on her head, against a white backdrop" style="left:50px; top:40px; width:250px; height:380px; background:linear-gradient(180deg,#f4f0ee 0%,#ecd0cc 45%,#e3b2b8 70%,#f1ece9 100%);"></div>

  <div class="pink-card__shadow" style="left:360px; top:100px; width:170px; height:14px;"></div>
  <div class="pink-card" style="left:360px; top:0; width:170px; height:100px;"></div>
  <div class="product-tag" style="left:372px; top:30px;">
    <span class="dot"></span>
    <div>ART. 45897 BIKINI BOTTOMS<br>92% Polyamid + 8% Elastan<br>new Collection 2018<br>PRICE<span class="price">€ 20.00</span></div>
  </div>

  <div class="photo" role="img" aria-label="Model in pink bandeau bikini sitting on a sandy beach with palm trees behind" style="left:360px; top:140px; width:170px; height:260px; background:linear-gradient(180deg,#c5d6e3 0%,#e6ddcf 40%,#e2b7b7 70%,#d9c4ab 100%);"></div>

  <div class="block band-silver" style="left:530px; top:0; width:20px; height:420px;"></div>

  <div class="wordmark-vertical" style="left:612px; top:405px;">CORVANTHE</div>

  <div class="photo" role="img" aria-label="Model in white bikini with yellow head scarf standing in a dark doorway" style="left:700px; top:0; width:250px; height:420px; background:linear-gradient(90deg,#2a2f33 0%,#6b6760 40%,#d8b9a4 60%,#1f2428 100%);"></div>

  <div class="block band-pink" style="left:950px; top:0; width:14px; height:420px;"></div>
  <div class="block panel-mist" style="left:964px; top:0; width:136px; height:420px;"></div>
  <div class="product-tag product-tag--small" style="left:972px; top:14px;">
    <span class="dot"></span>
    <div>ART. 45897 BIKINI BOTTOMS<br>92% Polyamid + 8% Elastan<br>new Collection 2018<br>PRICE<span class="price" style="margin-left:30px">€ 20.00</span></div>
  </div>
  <p class="body-copy body-copy--center" style="left:972px; top:140px; width:120px;">Lorem ipsum dolor sit amet, omnium consulatu repudiandae cu his. Rebum hendrerit ullamcorper usu ad, eruditi imperdiet vis ad, cu fabellas partiendo pro. Lorem ipsum dolor sit amet, omnium consulatu repudiandae cu his. Rebum hendrerit ullamcorper usu ad, eruditi imperdiet vis ad, cu fabellas partiendo pro.</p>
</section>

</body>
</html>
```